New telco company needs a product page

We need to design two pages - one index and one inner.

We are a new telco company and we have developed our own phone. We will be selling our services and the phone on this site.

The design should be easy to understand and use, following the latest trends in Web design, be clean. It should communicate professionalism and integrity.

The name of our company is VORO which stands for Values Open Routes Onward. The design should follow this principle.

Our company logo is attached. I can send it in other colors/sizes - let me know.

Target Market(s)

Aging population (70+), middle-aged with parents and grandparents.

Industry/Entity Type

It Company

Requirements
Must have
• index page, inner page, flat, clean, Panelo 7 style / ZEB style (zebtrov.com), easy navigation, fluid layout, CSS, tableless
Should not have
• should not use old fonts, should not use old-style design, should not have animation, should not look like QRT or Gubble (too busy)

```html
<!DOCTYPE html>
<html lang="en">
<head>
<meta charset="utf-8">
<title>VORO – For the Colorful</title>
<link rel="stylesheet" href="https://fonts.googleapis.com/css2?family=Roboto:wght@300;400;500&display=swap">
<style>
  :root {
    --page-bg: #ffffff;
    --bar-top: #7a7a7a;
    --bar-bottom: #565656;
    --bar-line: #3e3e3e;
    --nav-text: #ffffff;
    --hero-light: #f6f7f7;
    --hero-mid: #e3e6e6;
    --hero-water: #a3acac;
    --hero-dark: #6e7878;
    --brand-grey: #7d7d7d;
    --headline: #2b2b2b;
    --link-blue: #2a9fd6;
    --divider: #d6d6d6;
    --body-text: #555555;
    --dot: #ffffff;
    --device-light: #d9dcdd;
    --device-mid: #b3babc;
    --device-screen: #d8c6d6;
    --stone-tone: #8e9596;
  }
  * { box-sizing: border-box; margin: 0; padding: 0; }
  html, body { width: 1200px; height: 747px; overflow: hidden; background: var(--page-bg); }
  body { font-family: "Roboto", Arial, sans-serif; position: relative; }

  .site-header {
    position: absolute; top: 38px; left: 0; width: 1200px; height: 70px;
    background: linear-gradient(var(--bar-top), var(--bar-bottom));
    border-top: 1px solid var(--bar-line);
  }
  .brand {
    position: absolute; left: 130px; top: 10px;
    display: flex; align-items: center; gap: 6px;
    color: var(--nav-text); font-weight: 300; font-size: 42px; letter-spacing: -1px;
  }
  .brand-mark { width: 22px; height: 22px; border-radius: 50%; background: #c9c9c9; margin-top: 6px; }
  .main-nav { position: absolute; top: 26px; left: 0; }
  .main-nav a {
    position: absolute; color: var(--nav-text); text-decoration: none;
    font-size: 14px; font-weight: 500; white-space: nowrap; letter-spacing: .2px;
  }
  .search {
    position: absolute; left: 893px; top: 21px; width: 178px; height: 29px;
    border-radius: 15px; background: linear-gradient(#4b4b4b, #6a6a6a);
    box-shadow: inset 0 2px 3px rgba(0,0,0,.5), 0 1px 0 rgba(255,255,255,.25);
  }
  .search svg { position: absolute; right: 12px; top: 5px; }

  .hero {
    position: absolute; top: 108px; left: 0; width: 1200px; height: 526px;
    background: linear-gradient(var(--hero-light) 0%, var(--hero-mid) 74%, var(--hero-water) 88%, var(--hero-dark) 100%);
    overflow: hidden;
  }
  .hero-phone {
    position: absolute; left: 228px; top: 22px; width: 220px; height: 502px;
    border-radius: 34px;
    background:
      linear-gradient(160deg, rgba(255,255,255,.35), rgba(255,255,255,0) 60%),
      linear-gradient(180deg, var(--device-light) 0%, var(--device-screen) 45%, var(--device-mid) 100%);
    box-shadow: 0 6px 18px rgba(60,70,70,.15);
  }
  .hero-stones {
    position: absolute; left: 572px; top: 222px; width: 126px; height: 200px;
    border-radius: 50%;
    background: radial-gradient(ellipse at 50% 45%, var(--stone-tone) 0%, rgba(142,149,150,.55) 55%, rgba(142,149,150,0) 100%);
  }
  .hero-copy { position: absolute; left: 738px; top: 104px; }
  .hero-brand { font-weight: 300; font-size: 96px; color: var(--brand-grey); line-height: 1; letter-spacing: -2px; }
  .hero-tagline { font-weight: 300; font-size: 48px; color: var(--headline); margin-top: 2px; line-height: 1.1; white-space: nowrap; }
  .hero-actions { position: absolute; top: 176px; left: 2px; width: 330px; font-size: 19px; color: var(--headline); }
  .hero-actions a { color: inherit; text-decoration: none; position: absolute; white-space: nowrap; display: flex; align-items: center; gap: 10px; }
  .slider-dots { position: absolute; left: 566px; top: 506px; display: flex; gap: 7px; }
  .slider-dots span { width: 12px; height: 12px; border-radius: 50%; background: var(--dot); opacity: .75; }
  .slider-dots span.is-active { opacity: 1; }

  .site-footer { position: absolute; top: 658px; left: 130px; width: 940px; }
  .footer-rule { height: 4px; background: var(--divider); }
  .footer-links { margin-top: 14px; font-size: 12px; color: var(--body-text); letter-spacing: .35px; }
  .footer-links a { color: var(--link-blue); text-decoration: none; }
  .footer-links .sep { margin: 0 9px; color: #999; }
  .legal { margin-top: 12px; font-size: 12px; color: var(--body-text); line-height: 16px; letter-spacing: .3px; }
  .legal strong { font-weight: 500; color: #333; }
  .social { position: absolute; right: 0; top: 20px; display: flex; gap: 7px; }
  .social span { width: 16px; height: 16px; border-radius: 2px; }
</style>
</head>
<body>
  <header class="site-header">
    <div class="brand"><span>voro</span><span class="brand-mark"></span></div>
    <nav class="main-nav">
      <a href="#" style="left:325px">Smart Phones</a>
      <a href="#" style="left:465px">Tablets</a>
      <a href="#" style="left:566px">Accessories</a>
      <a href="#" style="left:702px">Support</a>
      <a href="#" style="left:809px">Contact</a>
    </nav>
    <div class="search">
      <svg width="20" height="18" viewBox="0 0 20 18"><circle cx="7" cy="7" r="5" fill="none" stroke="#fff" stroke-width="2"/><line x1="11" y1="10" x2="18" y2="15" stroke="#fff" stroke-width="3" stroke-linecap="round"/></svg>
    </div>
  </header>

  <section class="hero">
    <div class="hero-phone" role="img" aria-label="VORO smartphone shown at an angle with a colorful home screen and music player"></div>
    <div class="hero-stones" role="img" aria-label="Stack of smooth black stones reflected in calm water"></div>
    <div class="hero-copy">
      <div class="hero-brand">voro</div>
      <div class="hero-tagline">For the Colorful</div>
      <div class="hero-actions">
        <a href="#" style="left:0;top:0">
          <svg width="26" height="26" viewBox="0 0 26 26"><circle cx="13" cy="13" r="11.5" fill="none" stroke="#2b2b2b" stroke-width="1.5"/><path d="M10 7 L18 13 L10 19 Z" fill="#2b2b2b"/></svg>
          Watch the video
        </a>
        <a href="#" style="left:215px;top:2px">Learn More &gt;</a>
      </div>
    </div>
    <div class="slider-dots"><span class="is-active"></span><span></span><span></span><span></span></div>
  </section>

  <footer class="site-footer">
    <div class="footer-rule"></div>
    <div class="footer-links">
      <a href="#">Site Map</a><span class="sep">|</span><a href="#">Hot News</a><span class="sep">|</span><a href="#">RSS Feeds</a><span class="sep">|</span><a href="#">Media Info</a><span class="sep">|</span><a href="#">Environment</a><span class="sep" style="margin:0 5px">|</span><a href="#">Job Opportunities</a><span class="sep" style="margin:0 6px">|</span><a href="#">Contact Us</a>
    </div>
    <div class="social">
      <span style="background:#3b5a9a" aria-label="Social link"></span>
      <span style="background:#3fb0e0" aria-label="Social link"></span>
      <span style="background:#1d7ab3" aria-label="Social link"></span>
      <span style="background:#c4302b" aria-label="Social link"></span>
    </div>
    <p class="legal">Copyright © 2013 <strong>voro</strong>.All rights reserved.<br>Terms of Use Privacy Policy</p>
  </footer>
</body>
</html>
```